Stationery Design Project for Pell Co

Hi All,

We need you to design stationary for a new online financial services business. We have already got the logo designed and it is attached. If you would like it in any other formats please let me know. If you could also if possible, match the fonts in your design to that on the logo’s provided.

What we need:
- Business Card
- A4 Letter head
- A4 Folders
- PPT template (Title page and regular page)

And what ever else you want to throw in.

We are in the process of getting the web site designed, however below is a list of websites which we like which will give you an understanding of the style that we are going for.

- vantrela.com
- brimhollow.com
- quellaport.com
- tarnivex.com

I look forward to your seeing your design.

Industry/Entity Type

Financial

Requirements
Must have
• Outputs:
- Documents ready to print
- Generic editable information
- Pdf copies of the documents
- Word version of letterhead

```html
<!DOCTYPE html>
<html lang="en">
<head>
<meta charset="utf-8">
<title>Pell Co — A4 Folder</title>
<link href="https://fonts.googleapis.com/css2?family=Quicksand:wght@500;600&display=swap" rel="stylesheet">
<style>
  :root {
    --backdrop: #4a4a4a;
    --paper: #ebebeb;
    --orange: #f39325;
    --ocean: #0b7fa6;
    --ocean-clear: rgba(11, 127, 166, 0);
    --haze: rgba(150, 183, 204, 0.75);
    --navy: #1d3a54;
    --mist: #c9d7e3;
    --white: #ffffff;
  }
  html, body {
    margin: 0;
    padding: 0;
    width: 1200px;
    height: 849px;
    overflow: hidden;
    background: var(--backdrop);
    font-family: "Quicksand", sans-serif;
  }
  .folder {
    position: absolute;
    left: 25px;
    top: 65px;
    width: 1150px;
    height: 718px;
    background: var(--ocean);
    overflow: hidden;
  }
  .folder__header {
    position: absolute;
    left: 0; top: 0;
    width: 100%;
    height: 156px;
    background: var(--paper);
  }
  .folder__stripe {
    position: absolute;
    left: 0; top: 156px;
    width: 100%;
    height: 35px;
    background: var(--orange);
  }
  .folder__artwork {
    position: absolute;
    left: 0;
    top: 410px;
    width: 100%;
    height: 308px;
    background: linear-gradient(to top, var(--haze) 0%, var(--ocean-clear) 100%);
  }
  .folder__fold {
    position: absolute;
    left: 575px; top: 0;
    height: 100%;
    border-left: 1px dashed rgba(255,255,255,0.75);
  }
  .brand {
    position: absolute;
    left: 626px;
    top: 47px;
    display: flex;
    align-items: center;
    gap: 20px;
  }
  .brand__dot {
    width: 60px;
    height: 60px;
    border-radius: 50%;
    background: var(--orange);
  }
  .brand__name {
    font-size: 41px;
    font-weight: 600;
    color: var(--navy);
    letter-spacing: 0.5px;
  }
  .contact {
    position: absolute;
    top: 681px;
    height: 18px;
    display: flex;
    align-items: center;
    justify-content: center;
    font-size: 8px;
    font-weight: 500;
    letter-spacing: 0.4px;
    white-space: nowrap;
  }
  .contact--address {
    left: 576px;
    width: 288px;
    background: var(--orange);
    color: var(--white);
  }
  .contact--address strong { font-weight: 600; margin-right: 3px; }
  .contact--phone {
    left: 868px;
    width: 130px;
    background: var(--mist);
    color: var(--ocean);
  }
  .contact--email {
    left: 1002px;
    width: 130px;
    background: var(--mist);
    color: var(--ocean);
  }
</style>
</head>
<body>
  <div class="folder">
    <div class="folder__header"></div>
    <div class="folder__stripe"></div>
    <div class="folder__artwork" role="img" aria-label="Flowing pale blue wave artwork across the lower folder"></div>
    <div class="folder__fold"></div>

    <div class="brand">
      <span class="brand__dot"></span>
      <span class="brand__name">pellco.com</span>
    </div>

    <div class="contact contact--address"><strong>PELL CO PTY LTD</strong> | 27 Marlow Lane, Sydney NSW 2000</div>
    <div class="contact contact--phone">Phone | (02) 5550 0142</div>
    <div class="contact contact--email">info@pellco.com</div>
  </div>
</body>
</html>
```